Young and modern Electrical company working in the commercial arena.

Wanting a business card design thats modern and will last. Maybe Minimalist? Happy to look at changing my logo

Target Market(s)

Builders, Project Managers

Industry/Entity Type

Electrical

Contact Information for Business Card

Name
Address
Phone number
Job title

Logo Text

our name or just the logo i'm open to ideas

Font styles to use
Sans Serif

Requirements
Nice to have
• would like to keep the purple in our current logo. it's kinda unique to our market
Should not have
• Don't want it to be to busy. simple is best i think

```html
<!DOCTYPE html>
<html lang="en">
<head>
<meta charset="utf-8">
<title>Varden Electrical – Business Card</title>
<link rel="stylesheet" href="https://fonts.googleapis.com/css2?family=Montserrat:wght@400;500;700&display=swap">
<style>
  :root {
    --backdrop: #2b2c30;
    --card: #1e1b1f;
    --purple: #6a3fb5;
    --white: #ffffff;
    --muted: #d9d6de;
  }
  * { box-sizing: border-box; margin: 0; padding: 0; }
  html, body {
    width: 1200px; height: 900px; overflow: hidden;
    background: var(--backdrop);
    font-family: "Montserrat", sans-serif;
  }
  .stage {
    width: 1200px; height: 900px;
    display: flex; flex-direction: column;
    align-items: center; justify-content: center; gap: 56px;
  }
  .card {
    position: relative;
    width: 630px; height: 360px;
    background: var(--card);
    border-radius: 22px;
    overflow: hidden;
    border-top: 12px solid var(--purple);
    border-bottom: 12px solid var(--purple);
    box-shadow: 0 18px 40px rgba(0,0,0,0.45);
  }
  .wordmark { color: var(--white); font-weight: 700; text-transform: uppercase; line-height: 1; }
  .wordmark .line-main { display: block; letter-spacing: 2px; }
  .wordmark .line-sub { display: block; letter-spacing: 10px; }

  .card--front .wordmark {
    position: absolute; left: 0; right: 0; top: 50%;
    transform: translateY(-50%);
    text-align: center;
  }
  .card--front .line-main { font-size: 72px; }
  .card--front .line-sub { font-size: 20px; margin-top: 10px; padding-left: 10px; }

  .card--back { padding: 38px 46px; }
  .card--back .line-main { font-size: 40px; }
  .card--back .line-sub { font-size: 12px; letter-spacing: 7px; margin-top: 6px; }
  .person { margin-top: 30px; }
  .person-name { color: var(--white); font-size: 22px; font-weight: 500; letter-spacing: 1px; }
  .person-role { color: var(--purple); font-size: 13px; margin-top: 4px; }
  .contact { margin-top: 26px; list-style: none; }
  .contact li {
    display: flex; align-items: flex-start; gap: 12px;
    color: var(--muted); font-size: 15px; line-height: 1.45; margin-bottom: 10px;
  }
  .contact svg { flex: none; margin-top: 3px; }
</style>
</head>
<body>
<main class="stage">
  <section class="card card--front" aria-label="Card front">
    <div class="wordmark">
      <span class="line-main">Varden</span>
      <span class="line-sub">Electrical</span>
    </div>
  </section>

  <section class="card card--back" aria-label="Card back">
    <div class="wordmark">
      <span class="line-main">Varden</span>
      <span class="line-sub">Electrical</span>
    </div>
    <div class="person">
      <p class="person-name">MARCO DELLING</p>
      <p class="person-role">CEO | Owner</p>
    </div>
    <ul class="contact">
      <li>
        <svg width="14" height="14" viewBox="0 0 24 24" aria-hidden="true"><path fill="#6a3fb5" d="M6.6 10.8a15.1 15.1 0 0 0 6.6 6.6l2.2-2.2a1 1 0 0 1 1-.25 11.4 11.4 0 0 0 3.6.57 1 1 0 0 1 1 1V20a1 1 0 0 1-1 1A17 17 0 0 1 3 4a1 1 0 0 1 1-1h3.5a1 1 0 0 1 1 1c0 1.25.2 2.45.57 3.57a1 1 0 0 1-.25 1z"/></svg>
        <span>800 555 0178</span>
      </li>
      <li>
        <svg width="14" height="16" viewBox="0 0 24 28" aria-hidden="true"><path fill="#6a3fb5" d="M12 0a9 9 0 0 0-9 9c0 6.8 9 19 9 19s9-12.2 9-19a9 9 0 0 0-9-9zm0 12.5A3.5 3.5 0 1 1 12 5.5a3.5 3.5 0 0 1 0 7z"/></svg>
        <span>412 Harbor Lane<br>Eastfield 5678</span>
      </li>
    </ul>
  </section>
</main>
</body>
</html>
```